Business Card Design for ClearPathVitality

We need the new logo on a business card for 3 employees:
Nora Kettering, PhD, Advanced Instructor and Practitioner of SomaLink Integral Medicine (email: nora@clearpathvitality.com)
Ray Holm, Business Manager (email: ray@clearpathvitality.com)
Bea Marlowe, Administrative Assistant (email: bea@helixsense.com)

Target Market(s)

healthcare professionals

Industry/Entity Type

Alternative Medicine

Contact Information for Business Card

Names, titles, emails (names, titles, emails are in project description), phone, address, website, with logo and tagline. See below for address, phone, website: 418 Alder Ln, Bldg 12, Ste 305
Lindenport, CA 97241
612-555-2746
www.clearpathvitality.com
Tagline: Roots of Balance, Light of Renewal

Font styles to use
Other font styles liked:
• Gabriela

Colors
00a990
86cfc6
6b449b
b7a5cd
85abd2
abd036

Requirements
Must have
• Colors and style that match the logo design - shades such as blue, green, purple
• Compatible or same font as in the logo
Nice to have
• Nice if it goes with the theme of Nora's last business card - uploaded below
Should not have
• colors or style in conflict with the logo

```html
<!DOCTYPE html>
<html lang="en">
<head>
<meta charset="utf-8">
<title>ClearPathVitality — Business Card</title>
<link href="https://fonts.googleapis.com/css2?family=Marcellus&display=swap" rel="stylesheet">
<style>
  :root{
    --bg:#e9eaec;
    --green:#17955a;
    --teal:#127a78;
    --navy:#1a3c7a;
    --lime:#8cc63f;
    --white:#ffffff;
    --paper:#f4f5f6;
    --ink-light:#eaf4ef;
  }
  *{margin:0;padding:0;box-sizing:border-box}
  html,body{width:1200px;height:726px;overflow:hidden;background:var(--bg)}
  body{font-family:"Marcellus",serif;position:relative}
  .card{position:absolute;width:540px;height:310px;border-radius:3px;overflow:hidden;
        box-shadow:0 8px 22px rgba(0,0,0,.18)}
  .card--front{left:30px;top:208px;background:linear-gradient(160deg,var(--green) 0%,var(--teal) 45%,var(--navy) 100%);color:var(--white)}
  .card--back{left:630px;top:208px;background:linear-gradient(160deg,var(--green) 0%,var(--teal) 45%,var(--navy) 100%);color:var(--white)}

  .brand{display:flex;align-items:center;gap:14px}
  .brand__dot{width:58px;height:58px;border-radius:50%;flex:none}
  .brand__name{font-size:30px;letter-spacing:.5px;line-height:1;font-weight:400}

  .card--front .brand{position:absolute;left:0;right:0;top:108px;justify-content:center}
  .card--front .brand__dot{background:var(--white)}
  .card--front .tagline{position:absolute;left:0;right:0;bottom:34px;text-align:center;font-size:15px;letter-spacing:.3px}

  .back__art{position:absolute;inset:0}
  .back__brand{position:absolute;right:18px;top:78px;width:176px;flex-direction:column;gap:12px}
  .back__brand .brand__dot{background:var(--green);width:64px;height:64px}
  .back__brand .brand__name{color:var(--navy);font-size:20px;letter-spacing:.2px;white-space:nowrap}

  .person{position:absolute;left:26px;top:30px}
  .person__name{font-size:23px;letter-spacing:.3px;font-weight:400}
  .person__title{font-size:12.5px;line-height:1.3;margin-top:6px;color:var(--ink-light)}

  .contact{position:absolute;left:26px;top:150px;list-style:none;font-size:12.5px;line-height:1.45}
  .contact li{display:flex;align-items:flex-start;gap:8px}
  .contact svg{width:12px;height:12px;margin-top:3px;flex:none}
  .contact .indent{padding-left:20px}

  .back__tagline{position:absolute;left:26px;bottom:38px;font-size:13px;color:var(--navy)}
</style>
</head>
<body>

<section class="card card--front" aria-label="Card front">
  <div class="brand">
    <span class="brand__dot"></span>
    <span class="brand__name">ClearPathVitality</span>
  </div>
  <p class="tagline">Roots of Balance &nbsp;|&nbsp; Light of Renewal</p>
</section>

<section class="card card--back" aria-label="Card back">
  <svg class="back__art" viewBox="0 0 540 310" preserveAspectRatio="none" aria-hidden="true">
    <path d="M318 0 C268 110 330 225 540 262 L540 0 Z" fill="var(--green)"/>
    <path d="M332 0 C284 108 346 218 540 252 L540 0 Z" fill="var(--paper)"/>
    <rect x="0" y="246" width="440" height="30" fill="var(--lime)"/>
    <rect x="0" y="276" width="540" height="34" fill="var(--navy)"/>
  </svg>

  <div class="person">
    <h1 class="person__name">Nora Kettering, PhD,</h1>
    <p class="person__title">Advanced Instructor and<br>Practitioner of SomaLink<br>Integral Medicine</p>
  </div>

  <ul class="contact">
    <li><svg viewBox="0 0 12 12"><path d="M2 1h2l1 3-1.3 1a6 6 0 0 0 3.3 3.3L8 7l3 1v2a1 1 0 0 1-1 1A9 9 0 0 1 1 2a1 1 0 0 1 1-1z" fill="#fff"/></svg>612-555-2746</li>
    <li><svg viewBox="0 0 12 12"><rect x="1" y="2.5" width="10" height="7" fill="none" stroke="#fff"/><path d="M1 2.5l5 4 5-4" fill="none" stroke="#fff"/></svg>nora@clearpathvitality.com</li>
    <li><svg viewBox="0 0 12 12"><circle cx="6" cy="6" r="5" fill="none" stroke="#fff"/><ellipse cx="6" cy="6" rx="2" ry="5" fill="none" stroke="#fff"/><path d="M1 6h10" stroke="#fff"/></svg>www.clearpathvitality.com</li>
    <li class="indent">418 Alder Ln, Bldg 12, Ste 305</li>
    <li class="indent">Lindenport, CA 97241</li>
  </ul>

  <p class="back__tagline">Roots of Balance &nbsp;|&nbsp; Light of Renewal</p>

  <div class="brand back__brand">
    <span class="brand__dot"></span>
    <span class="brand__name">ClearPathVitality</span>
  </div>
</section>

</body>
</html>
```